How likely are people to engage in social distancing? We need a good illustration to show the data!

We surveyed U.S. adults March 20th - 24th, 2020 and asked how likely they were to engage in social distancing (and other COVID-19 related health behaviors). What did the survey find? Basically, most people intend to engage in social distancing behaviors (e.g., avoiding large crowds) and other behaviors that reduce the spread of COVID-19 (e.g., washing hands at least 20 seconds). When most people intend to engage in a behavior, then public health professionals try to leverage that to move more people to act.
Now we need innovative and professional images that attempt to communicate one or all of these findings. The specific findings are nicely summarized in the attached document. For example, 82% of participants intend to engage in social distancing.
What sort of visual are we looking for? Our preference is for an original illustration (or set of illustrations). Our preference is for (creative and powerful illustrations, but we are also open to the creative and well-executed infographics.
We need these images fast . We will award monetary prizes to the 3 best designs. If we like more than that, then we might purchase more (e.g., in past contests, we have purchased as many as 30 designs).
What we will need:
(1) The illustrations must be original and we will need the photoshop and/or illustrator files for all artwork.
(2) You can illustrate all of the findings or just one of them. We need creative approaches that do a lucid job of bringing the data to life. Most people intend to engage in these behaviors. How to communicate that? Corvantists and Halmerites do not differ in their intentions; how to communicate that?
(3) The illustration should say, somewhere: "Based on a survey of 400 U.S. adults conducted March 20 - 24th, 2020."

U.S. Adults

• Original illustrations based on the findings of the survey (see attached document).

```html
<!DOCTYPE html>
<html lang="en">
<head>
<meta charset="utf-8">
<title>Engage in social distancing: 82% intend to</title>
<link href="https://fonts.googleapis.com/css2?family=Roboto:wght@400;500;700;900&display=swap" rel="stylesheet">
<style>
  :root {
    --bg: #fd5520;
    --yellow: #fbeb2a;
    --white: #ffffff;
    --icon-ring: #6e0d0b;
    --icon-fill: #e89a7a;
    --divider: #f7c33a;
  }
  * { margin: 0; padding: 0; box-sizing: border-box; }
  html, body {
    width: 1200px;
    height: 1200px;
    overflow: hidden;
    background: var(--bg);
  }
  .poster {
    position: relative;
    width: 1200px;
    height: 1200px;
    background: var(--bg);
    font-family: "Roboto", Arial, sans-serif;
  }
  .kicker, .stat, .source {
    position: absolute;
    left: 0;
    width: 100%;
    text-align: center;
    color: var(--yellow);
  }
  .kicker {
    top: 94px;
    font-size: 45px;
    font-weight: 700;
  }
  .stat {
    top: 176px;
    font-size: 72px;
    font-weight: 700;
  }
  .headline {
    position: absolute;
    left: 0;
    top: 380px;
    width: 100%;
    color: var(--white);
    font-weight: 900;
    font-size: 80px;
    line-height: 1;
  }
  .headline-line {
    position: absolute;
    display: flex;
    justify-content: space-between;
  }
  .line-maintain { left: 194px; width: 812px; top: 0; }
  .line-social { left: 306px; width: 590px; top: 123px; }
  .line-distancing { left: 90px; width: 1022px; top: 246px; }

  .tips {
    position: absolute;
    top: 820px;
    left: 0;
    width: 100%;
    height: 190px;
  }
  .tip {
    position: absolute;
    top: 0;
    width: 220px;
    margin-left: -110px;
    text-align: center;
    color: var(--white);
  }
  .tip-icon {
    display: block;
    width: 130px;
    height: 130px;
    margin: 0 auto;
    border-radius: 50%;
    background: radial-gradient(circle, var(--icon-fill) 0 48%, var(--icon-ring) 50%);
  }
  .tip-label {
    margin-top: 18px;
    font-size: 20px;
    font-weight: 500;
    line-height: 1.2;
  }
  .divider {
    position: absolute;
    top: 8px;
    width: 2px;
    height: 172px;
    background: var(--divider);
  }
  .source {
    top: 1122px;
    font-size: 25px;
    font-weight: 500;
  }
</style>
</head>
<body>
<main class="poster">
  <p class="kicker">Engage in social distancing:</p>
  <p class="stat">82% intend to</p>

  <h1 class="headline" aria-label="Maintain social distancing">
    <span class="headline-line line-maintain"><span>M</span><span>A</span><span>I</span><span>N</span><span>T</span><span>A</span><span>I</span><span>N</span></span>
    <span class="headline-line line-social"><span>S</span><span>O</span><span>C</span><span>I</span><span>A</span><span>L</span></span>
    <span class="headline-line line-distancing"><span>D</span><span>I</span><span>S</span><span>T</span><span>A</span><span>N</span><span>C</span><span>I</span><span>N</span><span>G</span></span>
  </h1>

  <section class="tips">
    <div class="tip" style="left:163px">
      <span class="tip-icon" role="img" aria-label="Illustration of hands being washed with soap and water"></span>
      <p class="tip-label">Wash hands</p>
    </div>
    <span class="divider" style="left:262px"></span>
    <div class="tip" style="left:383px">
      <span class="tip-icon" role="img" aria-label="Illustration of a person covering a sneeze with a tissue"></span>
      <p class="tip-label">always cover your<br>cough or sneeze</p>
    </div>
    <span class="divider" style="left:504px"></span>
    <div class="tip" style="left:614px">
      <span class="tip-icon" role="img" aria-label="Illustration of a handshake crossed out with a prohibition sign"></span>
      <p class="tip-label">Avoid contact<br>with sick people</p>
    </div>
    <span class="divider" style="left:728px"></span>
    <div class="tip" style="left:826px">
      <span class="tip-icon" role="img" aria-label="Illustration of a white face mask"></span>
      <p class="tip-label">Use Mask</p>
    </div>
    <span class="divider" style="left:924px"></span>
    <div class="tip" style="left:1029px">
      <span class="tip-icon" role="img" aria-label="Illustration of a crowd of people"></span>
      <p class="tip-label">Avoid crowded<br>places</p>
    </div>
  </section>

  <p class="source">Based on a survey of 400 U.S. adults conducted March 20 - 24th, 2020.</p>
</main>
</body>
</html>
```